Business Card design for law firm = Juriskite Australia

We are seeking a new design for our business cards.
We are keeping our logo, which is attached.
We need space for
Name
Title
Address is , which is
Level 14
82 Penhallow Street
Sydney NSW 2000
Phone :
Mobile :
Fax :
Email :
DX :
website www.juriskite.com.au

Industry/Entity Type

Law Firm / Banking and Finance

Contact Information for Business Card

We are seeking a new design for our business cards. We are keeping our logo. We need space for Name Title Address is Level 14 82 Penhallow Street Sydney NSW 2000 Phone Mobile Fax Email DX website www.juriskite.com.au

Colors
0054AA
0677BA
7BADD7
CADEEF
E8F1F8

Requirements
Must have
• see our website for general feel www.juriskite.com.au

```html
<!DOCTYPE html>
<html lang="en">
<head>
<meta charset="utf-8">
<title>Juriskite Australia – Business Card</title>
<link href="https://fonts.googleapis.com/css2?family=Crimson+Text:wght@400&family=Open+Sans:wght@400&display=swap" rel="stylesheet">
<style>
  :root {
    --backdrop: #232323;
    --card: #f1f1f1;
    --card-edge: #e2e2e2;
    --navy: #1f3f8f;
    --brand-blue: #0a8fc4;
    --teal: #1a7fa8;
    --ink: #2b2b2b;
  }
  html, body {
    margin: 0;
    padding: 0;
    width: 1200px;
    height: 576px;
    overflow: hidden;
    background: var(--backdrop);
  }
  .canvas {
    position: relative;
    width: 1200px;
    height: 576px;
  }
  .card {
    position: absolute;
    top: 139px;
    width: 484px;
    height: 292px;
    border-radius: 10px;
    background: linear-gradient(180deg, #f4f4f4 0%, var(--card) 60%, var(--card-edge) 100%);
    box-sizing: border-box;
    font-family: "Crimson Text", Georgia, serif;
  }
  .card--front { left: 102px; }
  .card--back  { left: 596px; }

  .brand-square {
    position: absolute;
    background: var(--brand-blue);
  }
  .card--front .brand-square { left: 38px; top: 155px; width: 48px; height: 48px; }
  .brand-name {
    position: absolute;
    margin: 0;
    color: var(--navy);
    font-weight: 400;
    line-height: 1;
  }
  .card--front .brand-name { left: 37px; top: 211px; font-size: 31px; }
  .tagline {
    position: absolute;
    left: 38px;
    top: 250px;
    margin: 0;
    font-family: "Open Sans", Arial, sans-serif;
    font-size: 11px;
    letter-spacing: 0.4px;
    color: var(--teal);
  }

  .card--back .brand-square { left: 30px; top: 43px; width: 49px; height: 49px; }
  .card--back .brand-name { left: 90px; top: 56px; font-size: 22px; }

  .person-name {
    position: absolute;
    left: 27px;
    top: 178px;
    margin: 0;
    font-size: 18px;
    font-weight: 400;
    color: var(--navy);
    line-height: 1;
  }
  .person-title {
    position: absolute;
    left: 27px;
    top: 199px;
    margin: 0;
    font-size: 12.5px;
    color: var(--ink);
  }
  .contacts {
    position: absolute;
    left: 27px;
    top: 226px;
    display: flex;
    gap: 12px;
    font-size: 11.5px;
    color: var(--ink);
    line-height: 18px;
  }
  .contacts ul { list-style: none; margin: 0; padding: 0; }
  .contacts li { display: flex; align-items: center; gap: 6px; white-space: nowrap; }
  .contacts svg { width: 10px; height: 10px; fill: var(--brand-blue); flex: none; }
  .address { display: flex; gap: 6px; align-items: flex-start; }
  .address svg { margin-top: 4px; }
  .address p { margin: 0; }
</style>
</head>
<body>
<main class="canvas">
  <section class="card card--front" aria-label="Card front">
    <div class="brand-square"></div>
    <h1 class="brand-name">Juriskite</h1>
    <p class="tagline">strategic legal outsourcing</p>
  </section>

  <section class="card card--back" aria-label="Card back">
    <div class="brand-square"></div>
    <p class="brand-name">Juriskite</p>
    <h2 class="person-name">Sam Whitford</h2>
    <p class="person-title">Managing Director</p>
    <div class="contacts">
      <ul class="contact-col">
        <li><svg viewBox="0 0 10 10"><path d="M1 3 Q5 0 9 3 L8 4.5 L6.5 4 L6.5 3.2 Q5 2.8 3.5 3.2 L3.5 4 L2 4.5 Z M2 5 H8 V9 H2 Z"/></svg>02 9400 0155</li>
        <li><svg viewBox="0 0 10 10"><path d="M3 1 H7 V3.5 H3 Z M1 4 H9 V7.5 H7.5 V6 H2.5 V7.5 H1 Z M3 6.8 H7 V9 H3 Z"/></svg>02 9400 0166</li>
      </ul>
      <ul class="contact-col">
        <li><svg viewBox="0 0 10 10"><path d="M0.5 2 H9.5 V8 H0.5 Z M1.2 2.6 L5 5.6 L8.8 2.6" stroke="#f1f1f1" stroke-width="0.8"/></svg>sam.whitford@juriskite.com.au</li>
        <li><svg viewBox="0 0 10 10"><circle cx="5" cy="5" r="4.5"/><path d="M0.5 5 H9.5 M5 0.5 V9.5 M2 2.5 Q5 4 8 2.5 M2 7.5 Q5 6 8 7.5" stroke="#f1f1f1" stroke-width="0.7" fill="none"/></svg>https://www.juriskite.com.au</li>
      </ul>
      <div class="address">
        <svg viewBox="0 0 10 10"><path d="M5 0.5 A3.5 3.5 0 0 1 8.5 4 C8.5 6.5 5 9.5 5 9.5 C5 9.5 1.5 6.5 1.5 4 A3.5 3.5 0 0 1 5 0.5 Z"/><circle cx="5" cy="4" r="1.3" fill="#f1f1f1"/></svg>
        <p>Level 14 82 Penhallow St<br>Sydney NSW 2000</p>
      </div>
    </div>
  </section>
</main>
</body>
</html>
```